KELP clinical trial results infographic

We need an infographic which presents the results from the KELP research trial. It should be colourful and engaging, in understandable language and showing the steps to get to the results. This is to showcase the results to patients/the public/clinicians, giving a brief summary of what the study proved. The final design should have the KELP logo at the top (please see the logo on the attached Word document)
I have attached the required logos which need to be used (KELP - within the Word doc, Brindlemoor Injury and Acute Care, University of Caddering, QRV - see also their design pack attached) as well as an example from another study, PLUMBEX4, as an example of what the layout could look like. Please DO NOT use the content from the PLUMBEX4 example though, please instead use the content from the attached document 'InfographicDesignInformation_KELP_ArtHatchery_02Dec2025'. Please also include information about the funding in a footer at the bottom of the infographic (as per the above document).
Look and feel
Each slider illustrates characteristics of the customer's brand and the style your logo design should communicate.

```html
<!DOCTYPE html>
<html lang="en">
<head>
<meta charset="utf-8">
<title>KELP trial results</title>
<link href="https://fonts.googleapis.com/css2?family=Fira+Sans:ital,wght@0,400;0,600;0,700;0,800;1,400;1,700&display=swap" rel="stylesheet">
<style>
:root{
  --navy:#1f2f5c;
  --blue:#2b78c0;
  --yellow:#e5bb00;
  --pale:#c7dff3;
  --sky:#eaf3fb;
  --grey:#bdbdbd;
  --red:#e0542a;
  --ink:#1f2f5c;
}
*{margin:0;padding:0;box-sizing:border-box}
html,body{width:1200px;height:2523px;overflow:hidden}
body{font-family:"Fira Sans",Arial,sans-serif;color:var(--ink);background:#fff;position:relative}
.abs{position:absolute}
.hero-bg{left:0;top:0;width:1200px;height:620px;background:linear-gradient(180deg,var(--sky) 0%,#fff 100%)}
.swoosh{left:0;top:0}
.brand{left:58px;top:22px;color:var(--blue);font-weight:800;font-size:84px;line-height:80px;letter-spacing:2px}
.brand small{display:block;font-size:13px;line-height:16px;color:var(--navy);font-weight:700;letter-spacing:0}
.uni{left:983px;top:0;width:161px;height:160px;background:var(--navy);color:#fff;text-align:center}
.uni .dot{width:70px;height:70px;border-radius:50%;border:2px solid #fff;margin:14px auto 12px}
.uni .l1{font-size:12px;letter-spacing:1px}
.uni .l2{font-size:17px;font-weight:600;letter-spacing:1px}
.hero-art{left:47px;top:166px;width:364px;height:364px;border-radius:50%;background:#fff;padding:11px}
.hero-art div{width:100%;height:100%;border-radius:50%;background:linear-gradient(135deg,#3a86cc,#2368ad)}
.title{left:428px;top:190px;font-size:41px;line-height:53px;font-weight:700;color:var(--navy);width:590px}
.subtitle{left:428px;top:369px;font-size:25px;line-height:33px;font-style:italic;color:var(--blue);width:630px}
.intro{left:57px;top:650px;font-size:25.5px;line-height:33px;width:1080px}
.pill{background:var(--yellow);color:var(--navy);font-weight:700;font-size:27px;display:flex;align-items:center;border-radius:0 40px 40px 0;padding-left:56px}
.pill.center{border-radius:40px;justify-content:center;padding-left:0}
.col{top:1028px;width:254px;font-size:25.5px;line-height:33.2px}
.col b{font-weight:700}
.divider{top:897px;width:6px;height:405px;background:var(--grey)}
.icon{top:890px}
.band{left:0;width:1200px;background:var(--pale)}
.key{top:1420px;left:0;width:1200px;text-align:center;font-size:24px;line-height:32px;font-style:italic;font-weight:700;color:var(--navy)}
.crit h3{font-size:25px;font-weight:700;margin-bottom:0}
.crit ul{list-style:none}
.crit li{font-size:25.5px;line-height:33.2px;padding-left:33px;position:relative}
.crit li svg{position:absolute;left:0;top:6px}
.detail{font-size:25.5px;line-height:33px;display:flex;align-items:center;gap:18px}
.ph{background:var(--blue);border-radius:6px}
.details-box{left:663px;top:2094px;width:537px;height:95px;background:linear-gradient(90deg,#fff,var(--sky))}
.collect{left:60px;top:2203px;font-size:26px;line-height:33px;width:1100px}
.funding{top:2290px;height:92px;text-align:center;font-size:25px;line-height:33px;padding-top:12px;color:var(--navy)}
.partner{left:0;top:2398px;width:1200px;display:flex;justify-content:center;align-items:center;gap:10px;font-size:27px;color:#8a8a8a;letter-spacing:.5px}
.partner span.sq{width:38px;height:38px;background:#8a8a8a;display:inline-block}
.footer{left:0;top:2455px;width:1200px;height:68px;background:var(--navy);color:#fff;font-weight:700;font-size:27px;display:flex;justify-content:center;align-items:center;gap:14px}
</style>
</head>
<body>
<div class="abs hero-bg"></div>
<svg class="abs swoosh" width="1200" height="620" viewBox="0 0 1200 620">
  <path d="M-10 200 C 120 270, 240 420, 430 520 C 620 600, 900 600, 1210 470" fill="none" stroke="var(--yellow)" stroke-width="34"/>
</svg>

<div class="abs brand">KELP<small>EARLY LOADING AFTER ANKLE REPAIR</small></div>

<div class="abs uni"><div class="dot"></div><div class="l1">UNIVERSITY OF</div><div class="l2">CADDERING</div></div>

<div class="abs hero-art"><div role="img" aria-label="Illustration of the bones of a foot and ankle with a fracture"></div></div>

<h1 class="abs title">Patients can safely start walking soon after surgery on a broken ankle</h1>
<p class="abs subtitle">Early Loading after Ankle Repair. A randomised clinical trial of weight-bearing following operatively treated ankle fracture.</p>

<p class="abs intro">Ankle fractures are very common, and often require an operation. After surgery for ankle fracture, patients are usually advised to avoid walking for 6 weeks (delayed weight-bearing). An alternative is to walk 2 weeks after surgery (early weight-bearing)</p>

<div class="abs pill" style="left:0;top:796px;width:329px;height:68px">Study Summary</div>

<div class="abs icon ph" style="left:115px;width:70px;height:126px" role="img" aria-label="Icon of a person walking"></div>
<div class="abs icon ph" style="left:408px;width:110px;height:126px;background:linear-gradient(135deg,var(--blue) 80%,var(--red) 80%)" role="img" aria-label="Icon of a walking person crossed out"></div>
<svg class="abs icon" style="left:692px;top:904px" width="116" height="102" viewBox="0 0 116 102">
  <rect x="8" y="14" width="104" height="86" rx="8" fill="var(--blue)"/>
  <rect x="8" y="14" width="104" height="14" fill="#1f5e9c"/>
  <rect x="24" y="2" width="8" height="22" rx="3" fill="var(--blue)"/>
  <rect x="52" y="2" width="8" height="22" rx="3" fill="var(--blue)"/>
  <rect x="80" y="2" width="8" height="22" rx="3" fill="var(--blue)"/>
  <text x="58" y="80" text-anchor="middle" fill="#fff" font-family="Fira Sans,sans-serif" font-weight="800" font-style="italic" font-size="40">4M</text>
</svg>
<svg class="abs icon" style="left:960px;top:904px" width="110" height="110" viewBox="0 0 110 110">
  <circle cx="48" cy="48" r="40" fill="none" stroke="var(--blue)" stroke-width="12"/>
  <text x="46" y="66" text-anchor="middle" fill="var(--blue)" font-family="Fira Sans,sans-serif" font-weight="800" font-size="50">$</text>
  <rect x="74" y="44" width="14" height="34" fill="var(--blue)"/>
  <path d="M62 76 H100 L81 102 Z" fill="var(--blue)"/>
</svg>

<div class="abs divider" style="left:332px"></div>
<div class="abs divider" style="left:617px"></div>
<div class="abs divider" style="left:902px"></div>

<p class="abs col" style="left:55px">In this study, half of the patients were instructed that they should put as much weight through their affected leg as they felt comfortable and without causing pain.</p>
<p class="abs col" style="left:362px">The other half were instructed to <b>avoid putting any weight</b> through their operated leg <b>for 6 weeks after surgery.</b></p>
<p class="abs col" style="left:647px">After <b>4 months</b>, ankle function was similar, and the number of complications was similar, in the two groups.</p>
<p class="abs col" style="left:932px">The cost to the PHS and social services were also similar, with <b>slightly lower costs</b> in the early weight bearing group.</p>

<div class="abs band" style="top:1370px;height:153px"></div>
<div class="abs pill center" style="left:417px;top:1335px;width:406px;height:68px">Key Messages/Findings</div>
<p class="abs key">An early weight-bearing strategy is not inferior in terms of ankle function to a delayed<br>weight-bearing strategy. Early weight-bearing is also likely to be cost-effective.</p>

<div class="abs pill" style="left:0;top:1558px;width:495px;height:69px">Eligibility Criteria (if relevant)</div>

<div class="abs crit" style="left:55px;top:1648px;width:545px">
  <h3>Inclusion criteria:</h3>
  <ul>
    <li><svg width="22" height="22" viewBox="0 0 22 22"><circle cx="11" cy="11" r="10" fill="var(--blue)"/><path d="M6 11.5l3.5 3.5 6.5-7" fill="none" stroke="#fff" stroke-width="2.6"/></svg>Aged 18 or over</li>
    <li><svg width="22" height="22" viewBox="0 0 22 22"><circle cx="11" cy="11" r="10" fill="var(--blue)"/><path d="M6 11.5l3.5 3.5 6.5-7" fill="none" stroke="#fff" stroke-width="2.6"/></svg>Has had operative fixation for an unstable ankle fracture.</li>
    <li><svg width="22" height="22" viewBox="0 0 22 22"><circle cx="11" cy="11" r="10" fill="var(--blue)"/><path d="M6 11.5l3.5 3.5 6.5-7" fill="none" stroke="#fff" stroke-width="2.6"/></svg>Surgery was performed within 14 days of the injury.</li>
    <li><svg width="22" height="22" viewBox="0 0 22 22"><circle cx="11" cy="11" r="10" fill="var(--blue)"/><path d="M6 11.5l3.5 3.5 6.5-7" fill="none" stroke="#fff" stroke-width="2.6"/></svg>The treating surgeon considers that the participant might benefit from early weight-bearing.</li>
    <li><svg width="22" height="22" viewBox="0 0 22 22"><circle cx="11" cy="11" r="10" fill="var(--blue)"/><path d="M6 11.5l3.5 3.5 6.5-7" fill="none" stroke="#fff" stroke-width="2.6"/></svg>Able and willing to give informed consent.</li>
  </ul>
</div>
<div class="abs crit" style="left:609px;top:1648px;width:540px">
  <h3>Exclusion criteria:</h3>
  <ul>
    <li><svg width="22" height="22" viewBox="0 0 22 22"><circle cx="11" cy="11" r="10" fill="var(--red)"/><path d="M7 7l8 8M15 7l-8 8" stroke="#fff" stroke-width="2.6"/></svg>A lack of protective sensation<br>(e.g. peripheral neuropathy).</li>
    <li><svg width="22" height="22" viewBox="0 0 22 22"><circle cx="11" cy="11" r="10" fill="var(--red)"/><path d="M7 7l8 8M15 7l-8 8" stroke="#fff" stroke-width="2.6"/></svg>Inability to adhere to trial procedures.<br>Bilateral operatively treated ankle fractures.</li>
    <li><svg width="22" height="22" viewBox="0 0 22 22"><circle cx="11" cy="11" r="10" fill="var(--red)"/><path d="M7 7l8 8M15 7l-8 8" stroke="#fff" stroke-width="2.6"/></svg>Already in a trial for ankle fracture.</li>
    <li><svg width="22" height="22" viewBox="0 0 22 22"><circle cx="11" cy="11" r="10" fill="var(--red)"/><path d="M7 7l8 8M15 7l-8 8" stroke="#fff" stroke-width="2.6"/></svg>Patient has received a hindfoot nail to treat index fracture.</li>
  </ul>
</div>

<div class="abs pill" style="left:0;top:2013px;width:460px;height:70px">Study details (if relevant)</div>

<div class="abs details-box"></div>
<div class="abs detail" style="left:55px;top:2100px"><div class="ph" style="width:56px;height:82px" role="img" aria-label="Icon of a person with a walking frame"></div>Randomised<br>controlled trial</div>
<div class="abs detail" style="left:357px;top:2100px"><div class="ph" style="width:68px;height:62px" role="img" aria-label="Icon of a folder of documents"></div>A non-inferiority<br>study</div>
<div class="abs detail" style="left:675px;top:2100px"><div class="ph" style="width:88px;height:68px" role="img" aria-label="Icon of a group of people"></div><span><b>561 adults</b> recruited from 23<br>PHS hospitals in the UK</span></div>

<p class="abs collect">Ankle function, quality of life and complications were collected at <b>6 weeks, 4 months and 12 months</b> after surgery.</p>

<div class="abs band funding">Halvergate Institute for Health Studies, Patient Outcomes Grant programme<br>(HP-RB-0418-31542), supported by the HIHS Caddering Biomedical Research Centre</div>

<div class="abs partner"><span class="sq"></span>BRINDLEMOOR INJURY &amp; ACUTE CARE</div>

<div class="abs footer">
  <svg width="28" height="22" viewBox="0 0 28 22"><rect x="1" y="1" width="26" height="20" rx="3" fill="#fff"/><path d="M2 3l12 9 12-9" fill="none" stroke="var(--navy)" stroke-width="2.4"/></svg>
  bonejointcare@qrvmail.org
</div>
</body>
</html>
```